Oil & Gas Service Brochure

We need to create a brochure that highlights the benefits of one of our services to oil and gas wells. We have a word document that includes a summary of the service and its problem solving benefits as well as some photos. The task will be to create a brochure using this information and our company logo and color schemes. Additionally, copy editing and proofing is preferred.

Target Market(s)

Oil & Gas Well Operators

```html
<!DOCTYPE html>
<html lang="en">
<head>
<meta charset="utf-8">
<title>Clear Fire System Brochure</title>
<link rel="stylesheet" href="https://fonts.googleapis.com/css2?family=Montserrat:wght@400;500;600;700;800&family=Roboto+Condensed:wght@400;500;700&display=swap">
<style>
:root{
  --navy:#2b2f8c;
  --navy-deep:#1b1e63;
  --ink:#2a2a2a;
  --grey-text:#5b5b5b;
  --band:#efefef;
  --paper:#ffffff;
  --stage:#e7e8ea;
  --concrete-a:#b9b4ac;
  --concrete-b:#8d877e;
}
*{margin:0;padding:0;box-sizing:border-box}
html,body{width:1200px;height:1200px;overflow:hidden;background:var(--stage)}
.stage{position:relative;width:1200px;height:1200px}
.page{position:absolute;background:var(--paper);overflow:hidden}
.cover{left:227px;top:84px;width:368px;height:512px}
.overview{left:605px;top:84px;width:367px;height:512px}
.summary{left:227px;top:607px;width:368px;height:514px}
.contact{left:605px;top:607px;width:367px;height:514px}
.company{position:absolute;left:0;width:100%;top:26px;text-align:center;font:600 13.5px/1 Montserrat,sans-serif;letter-spacing:2.3px;color:var(--grey-text)}
.company.light{color:#fff}
.brand{position:absolute;left:0;width:100%;display:flex;align-items:center;justify-content:center;gap:7px;font:700 17px/1 Montserrat,sans-serif;letter-spacing:1.5px;color:var(--navy)}
.brand .dot{width:12px;height:12px;border-radius:50%;background:var(--navy)}
.art{position:absolute;left:0;top:0}
.cover-title{position:absolute;left:48px;top:222px;color:#fff;font-family:Montserrat,sans-serif}
.cover-title .main{font-weight:800;font-size:28px;line-height:25px}
.cover-title .sub{font-weight:700;font-size:19.5px;line-height:19.5px;margin-top:3px}
.cover-web{position:absolute;left:50px;top:466px;display:flex;align-items:center}
.cover-web .dot{width:14px;height:14px;border-radius:50%;background:var(--navy);margin-right:8px}
.cover-web span{font:400 6.5px/1 Montserrat,sans-serif;letter-spacing:3.4px;color:var(--grey-text)}
.cover-web .rule{width:103px;height:1px;background:var(--navy);margin-left:3px;margin-top:3px}
.ov-box{position:absolute;left:25px;top:102px;width:307px;height:310px;background:rgba(43,47,140,.93);color:#fff;padding:34px 13px 0 13px}
.ov-box h2{font:700 17px/1 Montserrat,sans-serif;margin-bottom:10px}
.ov-box p{font:700 6.1px/9.2px "Roboto Condensed",sans-serif;text-align:justify;text-indent:30px}
.steps{list-style:none;margin-top:16px;padding-left:18px;font:400 5.6px/14.9px "Roboto Condensed",sans-serif}
.sum-head{position:absolute;left:0;top:0;width:100%;height:114px;background:var(--navy)}
.sum-mark{position:absolute;left:32px;top:45px;width:15px;height:20px;background:var(--navy-deep)}
.sum-title{position:absolute;left:46px;top:46px;color:#fff;font:700 25px/1 Montserrat,sans-serif}
.sum-lead{position:absolute;left:46px;top:87px;width:290px;color:#fff;font:500 8px/9.5px "Roboto Condensed",sans-serif}
.benefits{position:absolute;left:80px;top:122px;width:258px;list-style:none;font:400 5.6px/14.9px "Roboto Condensed",sans-serif;color:var(--ink)}
.fill-photo{position:absolute}
.fill-block{position:absolute;background:var(--navy)}
.chart{position:absolute}
.caption{position:absolute;color:var(--navy);font:500 8px/9.4px "Roboto Condensed",sans-serif;text-align:justify}
.sum-caption{left:48px;top:467px;width:300px;text-indent:30px}
.ct-strip{position:absolute;left:96px;width:175px;background:var(--navy)}
.ct-band{position:absolute;left:0;top:20px;width:100%;height:69px;background:var(--band)}
.ct-caption{left:32px;top:287px;width:303px;text-indent:30px}
.touch{position:absolute;left:0;width:100%;top:320px;text-align:center;font:400 17px/1 Montserrat,sans-serif;color:var(--navy)}
.touch b{font-weight:700;color:#4a4a4a}
.touch-rule{position:absolute;left:161px;top:350px;width:44px;height:3px;background:var(--navy)}
.details{position:absolute;left:0;width:100%;top:373px;text-align:center;font:400 10.5px/20px Montserrat,sans-serif;color:#4a4a4a}
.details b{font-weight:600}
.ct-foot{position:absolute;left:0;top:446px;width:100%;height:68px;background:var(--navy);color:#fff;text-align:center;font:400 10px/68px Montserrat,sans-serif;letter-spacing:4.4px}
</style>
</head>
<body>
<main class="stage">

  <!-- Cover -->
  <section class="page cover">
    <p class="company">RIDGELINE OILFIELD SERVICES INC.</p>
    <div class="brand" style="top:66px"><span class="dot"></span>RIDGELINE</div>
    <svg class="art" width="368" height="512" viewBox="0 0 368 512">
      <defs>
        <linearGradient id="plant" x1="0" y1="0" x2="1" y2="1">
          <stop offset="0" stop-color="#6f86c4"/>
          <stop offset=".5" stop-color="#20357a"/>
          <stop offset="1" stop-color="#070c2a"/>
        </linearGradient>
      </defs>
      <rect x="0" y="107" width="368" height="27" fill="#efefef"/>
      <rect x="0" y="149" width="368" height="221" fill="var(--navy)"/>
      <polygon points="204,149 368,149 368,370 90,370" fill="url(#plant)" role="img" aria-label="Photo of industrial plant piping in blue tones"/>
      <polygon points="59,385 368,385 368,428 59,428 80,385" fill="url(#plant)" role="img" aria-label="Photo strip of industrial plant piping"/>
      <polyline points="210,134 343,385 0,385" fill="none" stroke="#fff" stroke-width="10"/>
      <polygon points="59,428 80,385 0,385 0,428" fill="#fff"/>
    </svg>
    <div class="cover-title">
      <div class="main">CLEAR<br>FIRE SYSTEM</div>
      <div class="sub">for Well Stimulation<br>and Scale Removal<br>Services</div>
    </div>
    <div class="cover-web"><span class="dot"></span><span>www.ridgelinedirection.com</span><span class="rule"></span></div>
  </section>

  <!-- Overview -->
  <section class="page overview">
    <div class="fill-photo" role="img" aria-label="Photo of a perforated sub with yellow paint resting on concrete" style="left:0;top:0;width:367px;height:512px;background:linear-gradient(120deg,var(--concrete-a),var(--concrete-b) 60%,#a59d72)"></div>
    <div style="position:absolute;left:0;top:0;width:100%;height:59px;background:var(--navy-deep)"></div>
    <div style="position:absolute;left:0;top:425px;width:100%;height:87px;background:rgba(43,47,140,.85)"></div>
    <p class="company light">RIDGELINE OILFIELD SERVICES INC.</p>
    <div class="ov-box">
      <h2>Overview:</h2>
      <p>The origin of this service started in the DJ Basin when we discovered a need to increase production on older producing Plunger Lift wells. We found that after multiple rig workovers, the issue was not in the wellbore itself, but that the Perf or Slotted Sub had become either scaled or sanded off choking the well down to very little or no flow. Realizing the issue was fixable without doing an expensive traditional Workover, we purchased a device that allows us to perform basic ballistic procedures safely off our Slickline units. There are no other standard mechanical or hydraulic slickline perforating tools that can accomplish this service available. A typical job would look something like this.</p>
      <ol class="steps">
        <li>1. MIRU Slickline, RIH and pull plunger noting tight spots</li>
        <li>2. RIH and pull BSSV-note depth of nipple so we can correlate to tubing tally and wellbore diagram</li>
        <li>3. RIH with “dummy run” (Spang Jars, Weight bars, Blind Box and Temperature Probe) drift through<br>Profile Nipples to determine Perf Sub depth, establish bottom hole temperature and to locate fluid level.</li>
        <li>4. Once depths, fluid level and temperature have been confirmed and we know we are deep enough to<br>get into the Perf Sub, RIHW Clear Fire System® and either perforate new holes using a RTG (Retrievable<br>Tubing Gun) or remove scale utilizing our Scale Pulse®.</li>
        <li>5. Free flow well to determine if new or more communication has been established.</li>
        <li>6. RIHW broach to production nipple. Reset production tools and turn well back to the client</li>
      </ol>
    </div>
  </section>

  <!-- Summary -->
  <section class="page summary">
    <div class="sum-head"></div>
    <p class="company light">RIDGELINE OILFIELD SERVICES INC.</p>
    <div class="sum-mark"></div>
    <h2 class="sum-title">Summary:</h2>
    <p class="sum-lead">This service can be done in a few hours if no unexpected well conditions are encountered. The main benefits are:</p>
    <ol class="benefits">
      <li>1. For a small investment, we can provide information on if the well needs to be worked over or not. IE<br>if we perform this service and nothing changes, you know you have wellbore issues-NOT production<br>tubing issues.</li>
      <li>2. This service is “greener” than a traditional workover by producing far less emissions. There is no need<br>to kill the well or to flare any gas.</li>
      <li>3. When the service is successful, the data has shown an increase of 100%-600% in production! For<br>example, we have stimulated wells that were making 2-3BBL/day before we performed this service, and<br>they are now producing 50-70BBL/day!</li>
      <li>4. This service is cost effective enough that in most cases, the “free” increased production will pay for<br>this service in 24-48 hours of running the well for 24-48 hours.</li>
    </ol>
    <div class="fill-block" style="left:2px;top:291px;width:54px;height:51px"></div>
    <div class="fill-photo" role="img" aria-label="Photo of a scaled perforated sub recovered from a workover rig" style="left:21px;top:277px;width:153px;height:79px;background:linear-gradient(135deg,#8d8a82,#54524d 55%,#a09c92)"></div>
    <svg class="chart" style="left:189px;top:284px" width="159" height="65" viewBox="0 0 159 65">
      <text x="80" y="5" text-anchor="middle" font-family="Roboto Condensed, sans-serif" font-size="3.6" fill="#4472c4">Scale Pulse Case Well #001 - Production BPD</text>
      <g stroke="#e3e3e3" stroke-width=".4">
        <line x1="12" y1="12" x2="155" y2="12"/><line x1="12" y1="20" x2="155" y2="20"/><line x1="12" y1="28" x2="155" y2="28"/><line x1="12" y1="36" x2="155" y2="36"/><line x1="12" y1="44" x2="155" y2="44"/>
      </g>
      <line x1="12" y1="46" x2="155" y2="46" stroke="#999" stroke-width=".4"/>
      <polyline fill="none" stroke="#4472c4" stroke-width=".8" points="12,40 18,44 24,41 30,45 36,39 42,42 48,38 54,41 60,37 66,42 72,39 78,41 84,40 90,24 96,29 102,26 108,29 114,26 120,27 126,27 132,29 138,26 144,27 150,29"/>
      <text x="4" y="32" font-family="Roboto Condensed, sans-serif" font-size="3" fill="#4a4" transform="rotate(-90 4 32)">BPD</text>
      <text x="80" y="62" text-anchor="middle" font-family="Roboto Condensed, sans-serif" font-size="3" fill="#4472c4">Date - service performed 5/11/2022</text>
    </svg>
    <svg class="chart" style="left:20px;top:385px" width="132" height="51" viewBox="0 0 132 51">
      <rect x=".5" y=".5" width="131" height="50" fill="#fff" stroke="#ddd" stroke-width=".5"/>
      <text x="56" y="5" text-anchor="middle" font-family="Roboto Condensed, sans-serif" font-size="2.6" fill="#4472c4">Average Daily Production Before / After Service - Case Well #002</text>
      <text x="56" y="9" text-anchor="middle" font-family="Roboto Condensed, sans-serif" font-size="2.6" fill="#2a9d3a">427% increase in production</text>
      <line x1="6" y1="20" x2="118" y2="20" stroke="#e3e3e3" stroke-width=".4"/>
      <line x1="6" y1="32" x2="118" y2="32" stroke="#e3e3e3" stroke-width=".4"/>
      <line x1="6" y1="44" x2="118" y2="44" stroke="#ccc" stroke-width=".4"/>
      <line x1="32" y1="41" x2="90" y2="18" stroke="#4472c4" stroke-width=".8"/>
      <text x="32" y="48" text-anchor="middle" font-family="Roboto Condensed, sans-serif" font-size="2.2" fill="#555">Before service</text>
      <text x="90" y="48" text-anchor="middle" font-family="Roboto Condensed, sans-serif" font-size="2.2" fill="#555">After service</text>
    </svg>
    <div class="fill-photo" role="img" aria-label="Photo of a yellow-painted perforated sub on a metal grate" style="left:162px;top:370px;width:188px;height:78px;background:linear-gradient(160deg,#6a675f,#3e3c37 45%,#c9c03a 70%,#7a7768)"></div>
    <div class="fill-block" style="left:314px;top:384px;width:54px;height:50px"></div>
    <p class="caption sum-caption">Images 1-2: Perforated Sub recovered from a Workover rig that was completely scaled off. I painted it yellow before the test to see how much scale came off when it was stimulated using our Scale Pulse.</p>
  </section>

  <!-- Contact -->
  <section class="page contact">
    <div class="ct-band"></div>
    <div class="ct-strip" style="top:2px;height:18px"></div>
    <p class="company">RIDGELINE OILFIELD SERVICES INC.</p>
    <div class="brand" style="top:57px;font-size:14px"><span class="dot" style="width:10px;height:10px"></span>RIDGELINE</div>
    <div class="ct-strip" style="top:89px;height:44px"></div>
    <div class="fill-photo" role="img" aria-label="Photo of a perforated sub after scale removal, showing its open holes" style="left:54px;top:133px;width:258px;height:141px;background:linear-gradient(150deg,#b8b2a6,#6f6b62 45%,#a79f4a 75%,#c2bba9)"></div>
    <p class="caption ct-caption">Perforated Sub after utilizing Scale Pulse. ALL scale removed from the sub opening the original 56 holes.</p>
    <h2 class="touch"><b>Get in</b> touch now</h2>
    <div class="touch-rule"></div>
    <div class="details">
      <p><b>Phone :</b> + 00 123 456 789</p>
      <p><b>Gmail :</b> yourmail@gmail.com</p>
      <p><b>Address :</b> Your Address Goes Here</p>
    </div>
    <div class="ct-foot">www.ridgelinedirection.com</div>
  </section>

</main>
</body>
</html>
```